Etiketten-Design für Himbeer-Gin
Zielgruppe
GIN
Aufgabenstellung
Wir benötigen ein Etikett für unseren neuen Himbeere GIN, der Name des GINs lautet: KorvalaGIN und soll für folgende Flasche dargestellt werden: https://www.flakoria-beispiel.de/luma-flasche-500ml-schwarz-beschichtet-tqx41-karton-48stk.html
mit dem Etikett https://klebmarken-beispiel.de/anwendungen/fluoreszierende-etiketten/ Himbeerlastiges Design mit bestehendem Logo (WendelGIN) siehe Daten. Bei Fragen stehe ich gerne zur Verfügung!

```html
<!DOCTYPE html>
<html lang="de">
<head>
<meta charset="utf-8">
<title>WendelGIN – Korvala Gin Etikett</title>
<link href="https://fonts.googleapis.com/css2?family=Cabin:wght@400;600&family=Open+Sans:wght@400&family=Oswald:wght@400;500&family=Roboto+Condensed:wght@400&display=swap" rel="stylesheet">
<style>
  :root {
    --page: #ffffff;
    --berry-deep: #7d0649;
    --berry-mid: #d92a85;
    --berry-soft: #cc4a93;
    --logo-grey: #e6e3e5;
    --pale-pink: #e9a5c9;
    --muted-pink: #dc92bb;
    --ghost-pink: #e77ab5;
    --ink-dark: #2c1120;
    --white: #ffffff;
    --info-fill: #f6f7f6;
  }
  * { box-sizing: border-box; margin: 0; padding: 0; }
  html, body { width: 1200px; height: 2400px; overflow: hidden; background: var(--page); }
  .canvas { position: relative; width: 1200px; height: 2400px; }

  .label {
    position: absolute;
    top: 755px;
    width: 520px;
    height: 890px;
    border-radius: 44px;
    overflow: hidden;
    background: linear-gradient(90deg, var(--berry-deep) 0%, var(--berry-mid) 55%, var(--berry-soft) 100%);
    box-shadow: 10px 12px 16px rgba(0,0,0,0.28);
    color: var(--white);
  }
  .label--front { left: 60px; }
  .label--back { left: 620px; }

  .abs { position: absolute; }
  .portrait {
    left: 195px; width: 130px; height: 150px;
    border-radius: 48% 48% 44% 44%;
    background: radial-gradient(circle at 50% 45%, rgba(245,170,210,0.85), rgba(220,110,170,0.35) 70%, transparent 100%);
  }
  .portrait--top { top: 0; }
  .portrait--bottom { top: 740px; opacity: 0.7; }

  .estd {
    font-family: "Cabin", sans-serif;
    font-size: 19px;
    color: var(--pale-pink);
    letter-spacing: 1px;
  }
  .wordmark {
    font-family: "Cabin", sans-serif;
    font-weight: 600;
    color: var(--logo-grey);
    white-space: nowrap;
    text-align: center;
  }
  .front-wordmark { left: 0; width: 520px; top: 190px; font-size: 92px; line-height: 1; }
  .ghost-wordmark { left: 0; width: 520px; top: 570px; font-size: 84px; line-height: 1; color: var(--ghost-pink); opacity: 0.4; }

  .region { left: 0; width: 520px; text-align: center; }
  .region-name { top: 380px; font-family: "Cabin", sans-serif; font-size: 34px; color: var(--muted-pink); letter-spacing: 1px; }
  .style-name { top: 425px; font-family: "Cabin", sans-serif; font-weight: 600; font-size: 27px; color: var(--pale-pink); }
  .variety { top: 468px; font-family: "Oswald", sans-serif; font-weight: 500; font-size: 40px; color: var(--ink-dark); letter-spacing: 5px; }

  .volume, .strength { font-family: "Roboto Condensed", sans-serif; font-size: 24px; color: var(--white); }
  .front-volume { left: 85px; top: 838px; }
  .front-strength { right: 80px; top: 840px; }

  .back-wordmark { left: 0; width: 520px; top: 65px; font-size: 76px; line-height: 1; }
  .copy {
    left: 30px; width: 460px; top: 230px;
    font-family: "Open Sans", sans-serif;
    font-size: 19px; line-height: 28px; letter-spacing: 2px;
    text-align: center; color: var(--white);
  }
  .copy-claim { font-family: "Roboto Condensed", sans-serif; font-size: 30px; letter-spacing: 3px; line-height: 44px; margin-top: 4px; }
  .copy-block { margin-top: 36px; }
  .copy-block + .copy-block { margin-top: 22px; }
  .copy-block--gap { margin-top: 36px; }

  .back-specs {
    left: 60px; top: 745px;
    font-family: "Roboto Condensed", sans-serif;
    font-size: 30px; line-height: 48px; letter-spacing: 4px; text-align: right;
  }
  .info-box { left: 200px; top: 745px; width: 275px; height: 104px; background: var(--info-fill); }
</style>
</head>
<body>
<main class="canvas">

  <section class="label label--front" aria-label="Etikett Vorderseite">
    <div class="abs portrait portrait--top" role="img" aria-label="Porträtfoto des Namensgebers, gerastert in Rosa"></div>
    <span class="abs estd" style="left:136px;top:98px;">ESTD.</span>
    <span class="abs estd" style="left:334px;top:98px;">2019</span>

    <div class="abs wordmark front-wordmark">WendelGIN</div>

    <div class="abs region region-name">SCHWÄBISCHER</div>
    <div class="abs region style-name">DRY GIN</div>
    <div class="abs region variety">KORVALA GIN</div>

    <div class="abs wordmark ghost-wordmark" aria-hidden="true">WendelGIN</div>
    <div class="abs portrait portrait--bottom" role="img" aria-label="Blasses Porträtfoto als Spiegelung"></div>

    <span class="abs volume front-volume">500 ml</span>
    <span class="abs strength front-strength">43% vol</span>
  </section>

  <section class="label label--back" aria-label="Etikett Rückseite">
    <div class="abs wordmark back-wordmark">WendelGIN</div>

    <div class="abs copy">
      <p>So muss ein fruchtiger Gin<br>einfach schmecken.<br>Für genußvolle Momente<br>in angenehmer Gesellschaft oder<br>alleine. Hochwertige und handverlesene<br>Zutaten machen unseren Wendel Gin<br>einfach</p>
      <p class="copy-claim">Himmlisch (korvala)</p>
      <p class="copy-block">Zutaten: Wasser, Gin, Himbeere,<br>Alkohol, Wacholder,</p>
      <p class="copy-block">www.wendelgin.de</p>
      <p class="copy-block copy-block--gap">Hersteller, Herstelleradresse</p>
    </div>

    <div class="abs back-specs">500 ml<br>43% vol</div>
    <div class="abs info-box" aria-hidden="true"></div>
  </section>

</main>
</body>
</html>
```